Pool Website

Need a simple front page and one internal page for a pool construction website. Please read the Must Have section for info. We uploaded 2 logos, one with color and one black and white. The colors you use in the logo can be changed, we used Century Gothic for the typing under the logo.

Nice clean design. The main back behind the site can be any color but we want the content back ground to be white.

We want a scrolling photo gallery (it doesn't have to scroll in your sample just know that's what we are envisioning) on the front page and the menu, and maybe a couple of photos down below to be clicked on such as this http://www.dellmorepools.example/

The 2ndary page would still have a header and menu and some type of cool design. Could be similar to this http://www.dellmorepools.example/about-us/awards.html

Also some other designs they like are here http://www.trelvacraft.example/14-examples-of-clean-modern-website-design-inspiration/ I realize not all of these could have a image scroller on the front page which is fine.

Please do not copy their site exactly though it must be different.

For now you can just use sample stock photography for your photos for the design but ultimately we will swap them out for our own photos so there will not be a need to purchase stock photography of pools.

Menus will include Home - About - Services - Gallery - Contact - Blog

The current site is http://www.gilesfentonpools.example/ we do not want it to look anything like this. It's way too dark and just not professional looking. We want this new site to look very slick and professional.

We also want a space for social networking logos etc.

I have also attached 2 zip files that contain photos that may be used in the design. You do not have to use them all but you are welcome to use a few. Most will be put in the photo gallery.

Colors: Blues, white, grays, black, etc.
Updates

Added several photos that can be used in the design. Obviously you do not have to use them all most will be in the photo gallery but you're welcome to use some for your design. 

Target Market(s)

People with money for residential pools or companies that want corporate pools. Are target location is Miami and California

Industry/Entity Type

Construction

Font styles to use
Serif
Sans Serif

Requirements
Must have
• Nice clean design. The main back behind the site can be any color but we want the content back ground to be white.

```html
<!DOCTYPE html>
<html lang="en">
<head>
<meta charset="utf-8">
<title>Giles Fenton Pools</title>
<link href="https://fonts.googleapis.com/css2?family=Source+Sans+3:wght@400;700&family=Questrial&display=swap" rel="stylesheet">
<style>
:root{
  --navy:#25295e;
  --teal:#00bfc9;
  --text:#3a3f5c;
  --body:#6b6d78;
  --band:#e4e4e6;
  --line:#dedede;
  --panel:#f7f7f8;
  --white:#ffffff;
}
*{margin:0;padding:0;box-sizing:border-box}
html,body{width:1200px;height:1000px;overflow:hidden;background:var(--white)}
body{position:relative;font-family:"Questrial",sans-serif;color:var(--text)}
.site-header{position:absolute;left:0;top:0;width:1200px;height:137px;background:var(--white);box-shadow:0 2px 6px rgba(0,0,0,.18);z-index:2}
.brand{position:absolute;left:133px;top:24px;width:122px;display:flex;flex-direction:column;align-items:center;gap:8px}
.brand-mark{width:46px;height:46px;background:var(--navy)}
.brand-name{font-family:"Source Sans 3",sans-serif;font-weight:700;color:var(--navy);font-size:15px;line-height:17px;letter-spacing:.4px;text-align:center}
.tagline{position:absolute;left:290px;top:32px;font-size:15px;color:var(--text);white-space:nowrap}
.tagline strong{font-family:"Source Sans 3",sans-serif;font-weight:700;color:var(--navy);font-size:15px}
.call{position:absolute;left:903px;top:31px;display:flex;align-items:center;gap:8px;font-size:16px;white-space:nowrap}
.call strong{font-family:"Source Sans 3",sans-serif;font-weight:700;color:var(--navy);font-size:17px;letter-spacing:.5px}
.main-nav{position:absolute;top:79px;left:0;width:1200px;height:31px}
.main-nav a{position:absolute;top:7px;font-size:15px;letter-spacing:1px;color:var(--text);text-decoration:none;text-transform:uppercase}
.main-nav a.active{top:0;left:443px;width:85px;height:31px;line-height:31px;text-align:center;background:var(--navy);color:var(--white);border-radius:3px;font-family:"Source Sans 3",sans-serif;font-weight:700;font-size:16px}
.hero{position:absolute;left:0;top:137px;width:1200px;height:418px;
  background:linear-gradient(180deg,#d9e6ee 0%,#b9c8c4 14%,#7f9b63 28%,#d8d0b8 45%,#6fb0d0 62%,#2f86bd 78%,#5c7a45 100%)}
.slider-bar{position:absolute;left:0;top:555px;width:1200px;height:47px;background:var(--band);box-shadow:0 3px 8px rgba(0,0,0,.12)}
.dots{position:absolute;left:578px;top:21px;display:flex;gap:4px}
.dots span{width:9px;height:9px;border-radius:50%;background:#b5b5bb}
.dots span.on{background:var(--navy)}
.social{position:absolute;top:16px;left:924px;display:flex;gap:34px}
.social span{width:16px;height:16px;background:#9c9ca3;border-radius:2px}
.offer{position:absolute;left:124px;top:641px;width:949px;height:68px;border:1px solid var(--line);background:var(--panel);border-radius:3px}
.offer-label{position:absolute;left:36px;top:16px;font-family:"Source Sans 3",sans-serif;font-weight:700;font-size:29px;color:var(--navy);white-space:nowrap}
.offer-text{position:absolute;left:262px;top:15px;font-size:30px;color:var(--navy);white-space:nowrap}
.offer-btn{position:absolute;left:746px;top:16px;width:167px;height:39px;line-height:39px;text-align:center;background:var(--teal);color:var(--white);border-radius:3px;font-family:"Source Sans 3",sans-serif;font-weight:700;font-size:15px;text-decoration:none}
.features{position:absolute;top:768px;left:0;width:1200px}
.feature{position:absolute;width:300px}
.feature h3{font-family:"Source Sans 3",sans-serif;font-weight:700;font-size:19px;line-height:22px;color:var(--navy)}
.feature p{margin-top:30px;font-size:13.5px;line-height:18px;color:var(--body)}
.projects-title{position:absolute;left:124px;top:948px;font-size:24px;font-weight:400;color:var(--text)}
.view-all{position:absolute;left:1004px;top:957px;width:71px;height:24px;line-height:24px;text-align:center;background:#c7c7cb;color:var(--white);font-size:9px;letter-spacing:.6px;border-radius:2px;text-decoration:none}
.project-thumb{position:absolute;top:995px;width:310px;height:20px}
</style>
</head>
<body>
<header class="site-header">
  <div class="brand">
    <div class="brand-mark"></div>
    <div class="brand-name">GILES FENTON<br>POOLS</div>
  </div>
  <p class="tagline"><strong>FAMILY OWNED FOR OVER 30 YEARS!</strong> Serving Broward, Palm &amp; Miami-Dade Counties</p>
  <div class="call">
    <svg width="18" height="14" viewBox="0 0 18 14" aria-hidden="true"><path d="M1 13 C2 6 7 5 11 5 V1 L17 7 L11 13 V9 C7 9 4 10 1 13Z" fill="var(--teal)"/></svg>
    <strong>CALL US</strong><span>954-555-0142</span>
  </div>
  <nav class="main-nav">
    <a class="active" href="#">Home</a>
    <a href="#" style="left:591px">About</a>
    <a href="#" style="left:692px">Services</a>
    <a href="#" style="left:814px">Gallery</a>
    <a href="#" style="left:931px">Blog</a>
    <a href="#" style="left:1024px">Contact</a>
  </nav>
</header>

<div class="hero" role="img" aria-label="Backyard pool with spa, palm trees and landscaped garden"></div>

<div class="slider-bar">
  <div class="dots"><span></span><span></span><span class="on"></span><span></span></div>
  <div class="social"><span></span><span></span><span></span><span></span></div>
</div>

<section class="offer">
  <span class="offer-label">SPECIAL OFFER</span>
  <span class="offer-text">Free Estimates &amp; Design Consults</span>
  <a class="offer-btn" href="#">Contact Us Today</a>
</section>

<section class="features">
  <div class="feature" style="left:130px">
    <h3>Family Owned<br>since 1979</h3>
    <p>Pellentesque habitant morbi tristique senectus<br>et netus et malesuada fames ac turpis egestas.<br>In elit lacus, pellentesque sed sollicitudin in,</p>
  </div>
  <div class="feature" style="left:450px">
    <h3>National Pool Builders<br>Guild Member</h3>
    <p>Pellentesque habitant morbi tristique senectus<br>et netus et malesuada fames ac turpis egestas.<br>In elit lacus, pellentesque sed sollicitudin in,</p>
  </div>
  <div class="feature" style="left:771px">
    <h3>Awarded over 75<br>NPBG Awards</h3>
    <p>Pellentesque habitant morbi tristique senectus<br>et netus et malesuada fames ac turpis egestas.<br>In elit lacus, pellentesque sed sollicitudin in,</p>
  </div>
</section>

<h2 class="projects-title">Recent Projects</h2>
<a class="view-all" href="#">VIEW ALL</a>
<div class="project-thumb" style="left:125px;background:linear-gradient(90deg,#6e8a5a,#b98a7a)" role="img" aria-label="Recent pool project photo"></div>
<div class="project-thumb" style="left:445px;background:linear-gradient(90deg,#8a6a5a,#5f7a4c)" role="img" aria-label="Recent pool project photo"></div>
<div class="project-thumb" style="left:765px;background:linear-gradient(90deg,#3aa8d0,#7fcbe0)" role="img" aria-label="Recent pool project photo"></div>
</body>
</html>
```